Coffee company needs coffee bag design!

Hi there!

Larkfield Bean Company is a new coffee roaster and cafe that is opening in 2016. We are currently seeking out a unique and exciting bag design that we can use for our 8 oz, gusset style coffee bags. These bags will be custom, full color printed with the design imprinted on each bag. We will use these for our in store retail sales, whole sales, and online mail order sales. The current size of the bag is 15 cm wide, and 22.5 cm tall. In addition to the full front print, we will use a separate printed label that will designate which coffee is in each bag, as well as tasting notes, and roast date. So there will need to be an area on the bag that can accommodate the label, whatever size it may be. We have a coffee tree logo that we would like incorporated into the design, however everything else is free game. We initially designed our logo to be a dark brown over a mint back ground. We would like to stick with those colors, but we don't have a set idea on layout or design. However it is important to note that our bag producer uses a plastic, matte finish material. So please try to incorporate a full color bag, not a kraft paper material. I would also like to add that we will potentially want to have this design incorporated into our cup design in some way.

Target Market(s)

Coffee enthusiasts and customers who are interested in specialty coffee. Specialty coffee denotes a premium bean, craft roasted in small batches. We pay special attention to sourcing directly with farmers that have been growing for generations. We are more interested in being a boutique premium brand, as opposed to a brand you would see in a grocery store.

Industry/Entity Type

Cafe

Font styles to use
Sans Serif
Other font styles liked:
• I'm open to any ideas that work well with our logo and idea.

Colors
86cfc6

Requirements
Must have
• Needs to incorporate our logo some how. Needs to have "8 oz. 227 grams" some where at the bottom of the bag for legal purposes. can be small. Would like to incorporate our colors of pastel mint and a darker brown.
Nice to have
• I really like the label designs of tovan and sons, peruvi salts, gilded fern, ashgrove cellar, denhart bros. Labels that convey a unique, small batch crafted product with an emphasis on quality over quantity.
Should not have
• Not a big fan of decorative fonts.

```html
<!DOCTYPE html>
<html lang="en">
<head>
<meta charset="utf-8">
<title>Larkfield Bean Company – 8 oz Coffee Bag</title>
<link href="https://fonts.googleapis.com/css2?family=Cormorant+Garamond:wght@500;600&display=swap" rel="stylesheet">
<style>
  :root {
    --roast-brown: #3a2a22;
    --mint: #d3ebe3;
    --mint-pale: #e4f1ec;
    --teal-line: #86cfc6;
    --label-ink: #3a2a22;
  }
  html, body {
    margin: 0;
    padding: 0;
    width: 720px;
    height: 1200px;
    overflow: hidden;
    background: var(--roast-brown);
  }
  .bag-front {
    position: relative;
    width: 720px;
    height: 1200px;
  }
  .bag-art {
    position: absolute;
    inset: 0;
    width: 720px;
    height: 1200px;
    display: block;
  }
  .brand-name {
    font-family: "Cormorant Garamond", serif;
    font-weight: 600;
    font-size: 30px;
    letter-spacing: 1px;
    fill: var(--label-ink);
  }
  .net-weight {
    font-family: "Cormorant Garamond", serif;
    font-weight: 500;
    font-size: 19px;
    fill: var(--mint-pale);
  }
</style>
</head>
<body>
<main class="bag-front">
  <svg class="bag-art" viewBox="0 0 720 1200" xmlns="http://www.w3.org/2000/svg">
    <defs>
      <linearGradient id="fade-to-mint" x1="0" y1="0" x2="0" y2="1">
        <stop offset="0" stop-color="var(--roast-brown)"/>
        <stop offset="1" stop-color="var(--mint-pale)"/>
      </linearGradient>
    </defs>

    <rect class="bag-ground" x="0" y="0" width="720" height="1200" fill="var(--roast-brown)"/>
    <rect class="top-rule" x="0" y="17" width="720" height="5" fill="var(--teal-line)"/>

    <path class="label-band-outline" fill="none" stroke="var(--teal-line)" stroke-width="5"
      d="M-10,296 H225 C255,296 275,232 360,228 C445,232 465,296 495,296 H730 V594 H495 C465,594 445,666 360,668 C275,666 255,594 225,594 H-10 Z"/>
    <path class="label-band" fill="var(--mint)"
      d="M0,310 H230 C260,310 280,248 360,244 C440,248 460,310 490,310 H720 V580 H490 C460,580 440,650 360,652 C280,650 260,580 230,580 H0 Z"/>

    <text class="brand-name" x="360" y="455" text-anchor="middle">Larkfield Bean Company</text>

    <ellipse class="bean-accent" role="img" aria-label="Small coffee bean accent" cx="115" cy="444" rx="13" ry="19" transform="rotate(20 115 444)" fill="var(--roast-brown)"/>
    <ellipse class="bean-accent" role="img" aria-label="Small coffee bean accent" cx="605" cy="444" rx="13" ry="19" transform="rotate(20 605 444)" fill="var(--roast-brown)"/>

    <rect class="lower-fade" x="0" y="790" width="720" height="320" fill="url(#fade-to-mint)"/>

    <rect class="base-strip" x="0" y="1110" width="720" height="56" fill="var(--roast-brown)"/>
    <path class="weight-tab" d="M262,1112 C262,1086 306,1068 360,1068 C414,1068 458,1086 458,1112 Z" fill="var(--roast-brown)"/>
    <text class="net-weight" x="360" y="1132" text-anchor="middle">8oz./227g</text>
    <rect class="base-rule" x="0" y="1170" width="720" height="5" fill="var(--teal-line)"/>
    <rect class="base-edge" x="0" y="1175" width="720" height="25" fill="var(--mint-pale)"/>
  </svg>
</main>
</body>
</html>
```